Modern looking signage for dental office.

Exterior signage for passing cars
Target Market(s)
Cars passing by
Font styles to use
Sans Serif
Colors
3276b5
Requirements
Must have
- Logo
- OPEN ON SUTURDAY AND SUNDAY
- NIGHT CLINIC AVAILABLE
- PLEASE USE THE FONT TYPE IN FILE 4 UPLOADED BELOW.
- (482) 730-2964
- Modern looking

```html
<!DOCTYPE html>
<html lang="en">
<head>
<meta charset="utf-8">
<title>Orven Dental – Exterior Sign</title>
<link rel="stylesheet" href="https://fonts.googleapis.com/css2?family=Fira+Sans:wght@300;400;600;700;800&display=swap">
<style>
  :root {
    --backdrop: #eceff1;
    --sign-white: #ffffff;
    --ink: #3a3637;
    --teal-deep: #17708f;
    --teal-mid: #1a8ea6;
    --teal-bright: #1f9db0;
    --teal-text: #17718f;
    --rule-light: rgba(255,255,255,0.55);
  }
  html, body {
    margin: 0;
    padding: 0;
    width: 1200px;
    height: 1000px;
    overflow: hidden;
    background: var(--backdrop);
    font-family: "Fira Sans", Arial, sans-serif;
  }
  .sign {
    position: absolute;
    left: 50px;
    top: 161px;
    width: 1100px;
    height: 678px;
    background: var(--sign-white);
    overflow: hidden;
    box-shadow: 0 6px 24px rgba(0,0,0,0.12);
  }
  .sign-waves {
    position: absolute;
    inset: 0;
  }
  .brand {
    position: absolute;
    left: 138px;
    top: 24px;
    display: flex;
    align-items: center;
  }
  .brand-circle {
    width: 176px;
    height: 176px;
    border: 3px solid var(--ink);
    border-radius: 50%;
    box-sizing: border-box;
    margin-right: 22px;
  }
  .brand-text {
    display: flex;
    flex-direction: column;
    align-items: center;
    padding-top: 20px;
  }
  .brand-name {
    font-weight: 400;
    font-size: 88px;
    line-height: 1;
    color: var(--ink);
    letter-spacing: 1px;
    white-space: nowrap;
  }
  .brand-tagline {
    margin-top: 16px;
    font-weight: 400;
    font-size: 35px;
    color: var(--ink);
    letter-spacing: 0.3px;
    white-space: nowrap;
  }
  .night-clinic {
    position: absolute;
    left: 288px;
    top: 264px;
    width: 524px;
    height: 72px;
    border-top: 2px solid var(--teal-text);
    border-bottom: 2px solid var(--teal-text);
    box-sizing: border-box;
    display: flex;
    align-items: center;
    justify-content: center;
    font-weight: 800;
    font-size: 44px;
    color: var(--teal-text);
    letter-spacing: 0.5px;
    white-space: nowrap;
  }
  .phone {
    position: absolute;
    left: 0;
    right: 0;
    top: 464px;
    display: flex;
    align-items: center;
    justify-content: center;
    gap: 26px;
    color: var(--sign-white);
  }
  .phone-icon {
    width: 76px;
    height: 76px;
  }
  .phone-number {
    font-weight: 600;
    font-size: 82px;
    line-height: 1;
    white-space: nowrap;
  }
  .divider {
    position: absolute;
    left: 50px;
    right: 50px;
    top: 606px;
    height: 2px;
    background: linear-gradient(90deg, transparent, var(--rule-light) 15%, var(--rule-light) 85%, transparent);
  }
  .weekend-hours {
    position: absolute;
    left: 0;
    right: 0;
    top: 614px;
    text-align: center;
    font-weight: 600;
    font-size: 45px;
    line-height: 56px;
    color: var(--sign-white);
    letter-spacing: 2px;
    white-space: nowrap;
  }
</style>
</head>
<body>
  <div class="sign">
    <svg class="sign-waves" width="1100" height="678" viewBox="0 0 1100 678">
      <defs>
        <radialGradient id="panelGlow" cx="0.5" cy="0.55" r="0.65">
          <stop offset="0" stop-color="var(--teal-bright)"/>
          <stop offset="1" stop-color="var(--teal-deep)"/>
        </radialGradient>
      </defs>
      <path d="M0,246 Q550,520 1100,246 L1100,678 L0,678 Z" fill="var(--teal-mid)"/>
      <path d="M0,260 Q550,548 1100,260 L1100,678 L0,678 Z" fill="var(--sign-white)"/>
      <path d="M0,270 Q550,566 1100,270 L1100,678 L0,678 Z" fill="url(#panelGlow)"/>
    </svg>

    <div class="brand">
      <div class="brand-circle"></div>
      <div class="brand-text">
        <div class="brand-name">ORVEN DENTAL</div>
        <div class="brand-tagline">MODERN GENERAL DENTISTRY</div>
      </div>
    </div>

    <div class="night-clinic">NIGHT CLINIC AVAILABLE</div>

    <div class="phone">
      <svg class="phone-icon" viewBox="0 0 78 78" aria-hidden="true">
        <circle cx="39" cy="39" r="36" fill="none" stroke="var(--sign-white)" stroke-width="4"/>
        <path d="M31,18 c-5,2 -8,6 -8,12 v18 c0,6 3,10 8,12 l4,-10 c-3,-1 -4,-3 -4,-6 v-10 c0,-3 1,-5 4,-6 z"
              fill="var(--sign-white)"/>
        <rect x="33" y="17" width="10" height="8" rx="2" fill="var(--sign-white)"/>
        <rect x="33" y="53" width="10" height="8" rx="2" fill="var(--sign-white)"/>
      </svg>
      <span class="phone-number">(482) 730-2964</span>
    </div>

    <div class="divider"></div>
    <div class="weekend-hours">OPEN ON SATURDAY AND SUNDAY</div>
  </div>
</body>
</html>
```